Electrician Business Card/ company logo/small business

New Business Cards and logo needed that will catch peoples eye and say we went that extra step. Attached is a design possibly to be incorporated, if u have your own great, lets see it!... This will be a small local business. thank you for all you do!
Corvane Electric
Wren Osloby Owner
Journeyman Electrician
phone 1.360.428.6037
email: KLXCorvaneElectric@mailvex.net
call for free estimate!

Target Market(s)

support small local business

Industry/Entity Type

Electrical,

Contact Information for Business Card

name, title,company/ logo, phone, email, free estimate

Font styles to use
Other font styles liked:
• easy to read

Colors

Designer to choose colors to be used in the design.

Requirements
Must have
• eye catching everything! logo and corvane electric listed on business card/logo, incorp logo in the background of card
Nice to have
• lightening bolts in eyes or around the triangle? vertical, modern, any design that would be unique and stand out
Should not have
• pinks, reds, yellows,brown

```html
<!DOCTYPE html>
<html lang="en">
<head>
<meta charset="utf-8">
<title>Corvane Electric – Business Card</title>
<link href="https://fonts.googleapis.com/css2?family=Audiowide&family=Exo+2:wght@600;700&family=Josefin+Sans:wght@300&display=swap" rel="stylesheet">
<style>
  :root {
    --stage: #e9eaee;
    --navy: #2c2f48;
    --panel: #1f4638;
    --panel-soft: #3f5a58;
    --green-dark: #1d5a3c;
    --green-bright: #22aa4c;
    --white: #ffffff;
  }
  html, body {
    margin: 0;
    width: 1200px;
    height: 1200px;
    overflow: hidden;
    background: var(--stage);
  }
  .sheet {
    width: 1200px;
    height: 1200px;
    display: flex;
    flex-direction: column;
    align-items: center;
    justify-content: space-evenly;
  }
  .card {
    width: 960px;
    height: 549px;
    display: block;
    box-shadow: 0 8px 24px rgba(20, 22, 40, 0.25);
  }
  .brand-title { font-family: "Audiowide", sans-serif; fill: var(--white); }
  .contact { font-family: "Exo 2", sans-serif; font-weight: 700; fill: var(--white); }
  .contact-light { font-family: "Josefin Sans", sans-serif; font-weight: 300; fill: var(--white); }
  .mark-name { font-family: "Audiowide", sans-serif; fill: var(--white); }
</style>
</head>
<body>
<main class="sheet">

  <!-- Card front -->
  <svg class="card card-front" viewBox="0 0 1050 600" role="img" aria-label="Corvane Electric business card front">
    <defs>
      <linearGradient id="greenBand" x1="0" y1="0" x2="1" y2="0">
        <stop offset="0" stop-color="var(--green-dark)"/>
        <stop offset="1" stop-color="var(--green-bright)"/>
      </linearGradient>
    </defs>
    <rect class="card-base" width="1050" height="600" fill="var(--navy)"/>

    <!-- top stripes -->
    <g class="top-stripes">
      <rect x="0" y="0" width="1050" height="62" fill="var(--navy)"/>
      <rect x="240" y="0" width="60" height="62" fill="var(--white)"/>
      <rect x="300" y="0" width="26" height="62" fill="var(--green-bright)"/>
      <rect x="370" y="0" width="70" height="62" fill="var(--white)"/>
      <rect x="440" y="0" width="22" height="62" fill="var(--green-bright)"/>
      <rect x="520" y="0" width="120" height="62" fill="var(--white)"/>
    </g>
    <rect class="top-rule" x="230" y="62" width="820" height="14" fill="var(--white)"/>

    <!-- central panel -->
    <polygon class="center-panel" points="360,76 1050,76 1050,480 600,480 360,330" fill="var(--panel)"/>
    <polygon class="green-band" points="600,76 1050,76 1050,160 650,160" fill="url(#greenBand)"/>
    <polygon class="soft-wedge" points="300,200 620,480 470,480 300,350" fill="var(--green-dark)" opacity="0.8"/>

    <!-- emblem frame -->
    <path class="emblem-frame" d="M0 338 H190 L330 220 L300 76" fill="none" stroke="var(--white)" stroke-width="14"/>
    <g class="emblem-mark">
      <rect x="40" y="150" width="28" height="28" fill="var(--white)"/>
      <text class="mark-name" x="80" y="175" font-size="28">Corvane</text>
      <text class="mark-name" x="40" y="215" font-size="28">Electric</text>
    </g>

    <text class="brand-title" x="1020" y="132" font-size="44" text-anchor="end">Corvane Electric</text>

    <!-- contact block -->
    <g class="contact-block" text-anchor="end">
      <text x="1010" y="228"><tspan class="contact" font-size="38">Wren Osloby </tspan><tspan class="contact-light" font-size="30">Owner</tspan></text>
      <text class="contact" x="1010" y="282" font-size="26">Journeyman Electrician</text>
      <rect x="960" y="300" width="50" height="3" fill="var(--white)"/>
      <text class="contact" x="1010" y="350" font-size="24">1.360.428.6037</text>
      <text class="contact" x="1010" y="392" font-size="22">KLXCorvaneElectric@mailvex.net</text>
    </g>

    <!-- bottom stripes -->
    <rect class="bottom-rule" x="520" y="480" width="530" height="14" fill="var(--white)"/>
    <g class="bottom-stripes">
      <rect x="560" y="494" width="80" height="106" fill="var(--white)"/>
      <rect x="672" y="494" width="28" height="106" fill="var(--white)"/>
      <rect x="760" y="494" width="90" height="106" fill="var(--white)"/>
      <rect x="890" y="494" width="30" height="106" fill="var(--white)"/>
      <rect x="980" y="494" width="70" height="106" fill="var(--white)"/>
    </g>
  </svg>

  <!-- Card back -->
  <svg class="card card-back" viewBox="0 0 1050 600" role="img" aria-label="Corvane Electric business card back">
    <defs>
      <linearGradient id="greenBandBack" x1="0" y1="0" x2="1" y2="0">
        <stop offset="0" stop-color="var(--green-dark)"/>
        <stop offset="1" stop-color="var(--green-bright)"/>
      </linearGradient>
    </defs>
    <rect class="card-base" width="1050" height="600" fill="var(--navy)"/>

    <g class="top-stripes">
      <rect x="240" y="0" width="60" height="62" fill="var(--white)"/>
      <rect x="300" y="0" width="26" height="62" fill="var(--green-bright)"/>
      <rect x="370" y="0" width="70" height="62" fill="var(--white)"/>
      <rect x="440" y="0" width="22" height="62" fill="var(--green-bright)"/>
      <rect x="520" y="0" width="120" height="62" fill="var(--white)"/>
    </g>
    <rect class="top-rule" x="230" y="62" width="820" height="14" fill="var(--white)"/>

    <polygon class="center-panel" points="0,76 1050,76 1050,330 0,330" fill="var(--panel)"/>
    <polygon class="soft-band" points="520,76 1050,76 1050,150 560,150" fill="var(--panel-soft)"/>
    <polygon class="green-band" points="720,250 1050,250 1050,330 760,330" fill="url(#greenBandBack)"/>

    <!-- faint background mark -->
    <rect class="faint-mark" x="150" y="110" width="190" height="190" fill="var(--white)" opacity="0.06"/>

    <text class="brand-title" x="70" y="195" font-size="78">Corvane</text>
    <text class="brand-title" x="70" y="280" font-size="78">Electric</text>

    <rect class="middle-rule" x="0" y="330" width="1050" height="14" fill="var(--white)"/>

    <!-- chevron -->
    <path class="chevron" d="M1050 344 H780 L600 460 V600" fill="none" stroke="var(--white)" stroke-width="14"/>
    <polygon class="chevron-fill" points="520,344 780,344 600,460 600,600 520,600" fill="var(--green-dark)" opacity="0.7"/>

    <g class="bottom-stripes">
      <rect x="640" y="500" width="70" height="100" fill="var(--white)"/>
      <rect x="750" y="500" width="28" height="100" fill="var(--white)"/>
      <rect x="830" y="500" width="80" height="100" fill="var(--white)"/>
      <rect x="960" y="500" width="30" height="100" fill="var(--white)"/>
    </g>
  </svg>

</main>
</body>
</html>
```